Need simple and modern looking business card with all my information on one side and logo on the other side
Info :
Company name - VELTRIN CONSTRUCTION LLC
Company addres- 418 maple 307th. Dunford hill ny 10583
Email- veltrinllc@pormail.Com
Company phone number 555-318-4096
Cell number- 555-762-0384
Web site - veltrinllc.Com
My name Gerald haverstrom

Target Market(s)

Construction , home improvement, remodeling

Industry/Entity Type

Construction

Contact Information for Business Card

It has to be moder but at the same time simple

Font styles to use
Sans Serif

Colors
0255a3
ffffff
000000
f78f20
b1b1b1
9d9d9d
1b1b1b
33a6d7
ec1f27

Requirements
Must have
• My logo on one side maybe with a some kind of background on the other side all my information
Nice to have
• Some kind of background pictures provided by you .PLEASE HAVE ACCOUNT WITH PIXVALEMOR WILL NOT PAY ANY EXTRA FEES .
Should not have
• Any kind of hamer, nails,screws, helmets itp. Please do not copy the other designs come up with something new.

```html
<!DOCTYPE html>
<html lang="en">
<head>
<meta charset="utf-8">
<title>Veltrin Construction LLC – Business Card</title>
<link rel="stylesheet" href="https://fonts.googleapis.com/css2?family=Saira:wght@500&display=swap">
<style>
  :root {
    --page-bg: #e6e6e6;
    --card-white: #ffffff;
    --brick-orange: #f39a1e;
    --brick-orange-deep: #e8860f;
    --tear-edge: #d9d9d9;
    --ink: #1b1b1b;
  }
  html, body {
    margin: 0;
    padding: 0;
    width: 1200px;
    height: 1000px;
    overflow: hidden;
    background: var(--page-bg);
  }
  .canvas {
    position: relative;
    width: 1200px;
    height: 1000px;
  }
  .card {
    position: absolute;
    left: 100px;
    top: 220px;
    width: 1000px;
    height: 560px;
    background: var(--card-white);
    overflow: hidden;
    box-shadow: 0 6px 24px rgba(0, 0, 0, 0.18);
  }
  .card__texture {
    position: absolute;
    inset: 0;
    width: 1000px;
    height: 560px;
  }
  .brand {
    position: absolute;
    right: 62px;
    top: 300px;
    text-align: right;
    font-family: "Saira", sans-serif;
    font-weight: 500;
    color: var(--ink);
    line-height: 1;
  }
  .brand__name {
    display: block;
    font-size: 128px;
    letter-spacing: 4px;
  }
  .brand__tagline {
    display: block;
    margin-top: 8px;
    font-size: 50px;
    letter-spacing: 5px;
  }
</style>
</head>
<body>
<main class="canvas">
  <section class="card">
    <svg class="card__texture" viewBox="0 0 1000 560" xmlns="http://www.w3.org/2000/svg">
      <defs>
        <linearGradient id="brickTone" x1="0" y1="0" x2="1" y2="1">
          <stop offset="0" stop-color="var(--brick-orange)"/>
          <stop offset="1" stop-color="var(--brick-orange-deep)"/>
        </linearGradient>
      </defs>
      <polyline class="card__tear-lip" fill="none" stroke="var(--tear-edge)" stroke-width="6"
        points="945,0 910,20 874,33 838,48 802,70 762,84 722,104 691,117 651,133 611,155 571,170 531,191 491,205 451,227 411,241 371,263 331,277 291,300 251,315 211,335 171,351 131,373 91,387 51,405 21,411 0,417"/>
      <polygon class="card__brick-wall" role="img" aria-label="Orange painted brick wall texture"
        fill="url(#brickTone)"
        points="0,0 940,0 905,18 870,30 835,44 800,66 760,80 720,100 690,112 650,128 610,150 570,165 530,186 490,200 450,222 410,236 370,258 330,272 290,295 250,310 210,330 170,346 130,368 90,382 50,400 20,406 0,412"/>
    </svg>
    <div class="brand">
      <span class="brand__name">VELTRIN</span>
      <span class="brand__tagline">CONSTRUCTION LLC</span>
    </div>
  </section>
</main>
</body>
</html>
```